Construction material supplies company business card ****

1. Full company name “Marlow Aggregate Products Ltd”
I am after a Business card design for the company as a whole. We are better known in Solomon Islands as “Marlow Aggregate” for short.

We are a building materials supplier of
Ready Mixed Concrete, Bricks and Blocks,
Quarry products- gravel, aggregates, sand etc.
Cement distributor/retailer of reputable brands.
Other prefab concrete products. Culverts, wave breakers, concrete retaining blocks etc.

2. Competitive Advantage over Competition: Quality, efficient, professional, dependable, reliable

3. We want people to feel trust worthy, high quality, strong when they see our brand

5. No preference to color. Maybe more sturdy and corporate. Not fancy.

Industry/Entity Type

CONSTRUCTION SUPPLY

Contact Information for Business Card

Name, Position, office phone mob phone, email

Requirements
Must have
• the company logo
Nice to have
• would like to see a mixture of designs, of with logo only and also with simple graphic designs to bring out the company whilst still have the strong sturdy professional feeling

```html
<!DOCTYPE html>
<html lang="en">
<head>
<meta charset="utf-8">
<title>Marlow Aggregate – Business Card</title>
<link href="https://fonts.googleapis.com/css2?family=Roboto:wght@400;500;700&display=swap" rel="stylesheet">
<style>
  :root {
    --backdrop: #2a2a2b;
    --concrete-light: #ececec;
    --concrete-mid: #dcdcdc;
    --concrete-dark: #cfcfcf;
    --emboss: #bfbfbf;
    --navy: #163b5e;
    --white: #ffffff;
  }
  * { margin: 0; padding: 0; box-sizing: border-box; }
  html, body {
    width: 1200px; height: 1138px; overflow: hidden;
    background: var(--backdrop);
    font-family: "Roboto", Arial, sans-serif;
  }
  .card {
    position: absolute;
    width: 622px; height: 375px;
    border-radius: 16px;
    overflow: hidden;
    color: var(--navy);
  }
  .card--front { left: 274px; top: 186px; }
  .card--back { left: 276px; top: 608px; }

  .concrete {
    position: absolute; inset: 0;
    background:
      radial-gradient(ellipse 40% 30% at 20% 25%, rgba(255,255,255,0.35), transparent 70%),
      radial-gradient(ellipse 35% 25% at 75% 70%, rgba(0,0,0,0.04), transparent 70%),
      radial-gradient(ellipse 30% 40% at 60% 20%, rgba(0,0,0,0.03), transparent 70%),
      radial-gradient(ellipse at 45% 40%, var(--concrete-light), var(--concrete-mid) 70%, var(--concrete-dark));
  }

  .front-brand {
    position: absolute; left: 0; right: 0; top: 124px;
    display: flex; justify-content: center; align-items: center; gap: 16px;
    color: var(--emboss);
  }
  .front-brand-mark { width: 40px; height: 40px; background: var(--emboss); }
  .front-brand-name { font-size: 40px; font-weight: 700; }
  .front-web {
    position: absolute; left: 0; right: 0; top: 333px;
    text-align: center;
    font-size: 15px; letter-spacing: 7px;
  }

  .brand {
    position: absolute; left: 40px; top: 72px; width: 270px;
    display: flex; flex-direction: column; align-items: center; gap: 22px;
  }
  .brand-mark { width: 72px; height: 72px; background: var(--navy); }
  .brand-name { font-size: 30px; font-weight: 700; white-space: nowrap; }

  .person {
    position: absolute; right: 36px; top: 52px;
    text-align: right;
  }
  .person-name { font-size: 23px; font-weight: 700; }
  .person-role { font-size: 16px; margin-top: 4px; }
  .person-address { font-size: 16px; line-height: 26px; margin-top: 20px; }

  .wave { position: absolute; left: 0; top: 0; }

  .contact {
    position: absolute; right: 30px; top: 268px;
    list-style: none; color: var(--white);
    font-size: 16px; text-align: right;
  }
  .contact li {
    display: flex; justify-content: flex-end; align-items: center;
    gap: 14px; height: 26px;
  }
  .contact svg { width: 14px; height: 14px; }
</style>
</head>
<body>

<section class="card card--front">
  <div class="concrete" role="img" aria-label="Grey concrete surface texture"></div>
  <div class="front-brand">
    <span class="front-brand-mark"></span>
    <span class="front-brand-name">Marlow Aggregate</span>
  </div>
  <div class="front-web">www.marlowaggregate.com</div>
</section>

<section class="card card--back">
  <div class="concrete" role="img" aria-label="Grey concrete surface texture"></div>
  <svg class="wave" width="622" height="375" viewBox="0 0 622 375">
    <path d="M0,324 C130,350 250,315 360,258 C450,214 540,200 622,206 L622,375 L0,375 Z" fill="#163b5e"/>
    <path d="M0,336 C140,356 260,330 370,272 C460,226 540,214 622,222" fill="none" stroke="#ffffff" stroke-width="0" />
    <path d="M55,320 C180,336 280,306 380,256 C460,218 540,208 622,214" fill="none" stroke="#e4e4e4" stroke-width="5"/>
    <path d="M55,304 C170,314 270,284 370,236 C450,200 540,192 622,196" fill="none" stroke="#163b5e" stroke-width="5"/>
  </svg>

  <div class="brand">
    <span class="brand-mark"></span>
    <span class="brand-name">Marlow Aggregate</span>
  </div>

  <div class="person">
    <div class="person-name">Daniel Hartley</div>
    <div class="person-role">Managing Director</div>
    <div class="person-address">18 Kukum Highway, Honiara,<br>Guadalcanal, SB 00100</div>
  </div>

  <ul class="contact">
    <li>000 0000 0000
      <svg viewBox="0 0 14 14"><path d="M2 4 Q7 0 12 4 L11 6 L9 5 L9 4 Q7 3 5 4 L5 5 L3 6 Z M3 7 H11 L12 12 H2 Z" fill="#ffffff"/></svg>
    </li>
    <li>daniel@marlowaggregate.com
      <svg viewBox="0 0 14 14"><rect x="1" y="3" width="12" height="8" fill="#ffffff"/><path d="M1 3 L7 8 L13 3" fill="none" stroke="#163b5e" stroke-width="1"/></svg>
    </li>
    <li>www.marlowaggregate.com
      <svg viewBox="0 0 14 14"><circle cx="7" cy="7" r="6" fill="#ffffff"/><path d="M1 7 H13 M7 1 V13 M7 1 Q3 7 7 13 M7 1 Q11 7 7 13" fill="none" stroke="#163b5e" stroke-width="0.8"/></svg>
    </li>
  </ul>
</section>

</body>
</html>
```